Tidewell Outdoor Signage

We need an outdoor signage design for my company with new logo designed from makerhive. We do electrical, Air conditioning & Plumbing, installation, service, repairs and maintenance. The design shall be an eye catching that cannot miss ready it.

Industry/Entity Type

Electrical, Air conditioning, Plumbing

```html
<!DOCTYPE html>
<html lang="en">
<head>
<meta charset="UTF-8">
<title>Tidewell Outdoor Signage</title>
<link href="https://fonts.googleapis.com/css2?family=Montserrat:wght@700;800&family=Open+Sans:wght@700&display=swap" rel="stylesheet">
<style>
  :root {
    --blue: #186bb0;
    --orange: #f08b42;
    --red: #e5252a;
    --white: #ffffff;
    --ink: #1a1a1a;
    --backdrop: #3c3b3b;
  }
  * { margin: 0; padding: 0; box-sizing: border-box; }
  html, body { width: 1200px; height: 655px; overflow: hidden; background: var(--backdrop); }
  .sign {
    position: absolute; left: 0; top: 27px;
    width: 1200px; height: 600px;
    display: flex;
  }
  .sign__main {
    position: relative; width: 727px; height: 100%;
    background: var(--white);
  }
  .sign__divider { width: 15px; height: 100%; display: flex; flex-direction: column; }
  .sign__divider-top { flex: 0 0 317px; background: var(--orange); }
  .sign__divider-bottom { flex: 1; background: var(--red); }
  .sign__services {
    position: relative; flex: 1; height: 100%;
    background: var(--blue); color: var(--white);
  }

  .brand {
    position: absolute; left: 0; right: 0; top: 175px;
    display: flex; align-items: center; justify-content: center; gap: 22px;
  }
  .brand__dot { width: 70px; height: 70px; border-radius: 50%; background: var(--orange); }
  .brand__name {
    font-family: "Montserrat", sans-serif; font-weight: 800;
    font-size: 118px; line-height: 1; letter-spacing: -3px;
    color: var(--blue);
  }
  .trades {
    position: absolute; left: 0; right: 0; top: 398px;
    display: flex; justify-content: center; gap: 18px;
    font-family: "Open Sans", sans-serif; font-weight: 700; font-size: 29px;
  }
  .trades__electrical { color: var(--red); }
  .trades__air { color: var(--blue); }
  .trades__plumbing { color: var(--orange); }

  .call-rule {
    position: absolute; left: 77px; width: 580px; top: 460px; height: 30px;
    display: flex; align-items: center; gap: 14px;
  }
  .call-rule__line { flex: 1; height: 2px; background: var(--ink); }
  .call-rule__icon {
    width: 38px; height: 38px; border-radius: 50%; background: var(--red);
    display: flex; align-items: center; justify-content: center;
  }
  .phone {
    position: absolute; left: 0; right: 0; top: 496px; text-align: center;
    font-family: "Montserrat", sans-serif; font-weight: 800;
    font-size: 72px; letter-spacing: 1px; color: var(--blue);
  }

  .service-list { position: absolute; left: 40px; top: 88px; list-style: none; }
  .service {
    position: relative; display: flex; align-items: center;
    font-family: "Montserrat", sans-serif; font-weight: 800;
    font-size: 38px; line-height: 1.08; text-transform: uppercase;
  }
  .service + .service { margin-top: 28px; }
  .service__badge {
    flex: 0 0 66px; width: 66px; height: 66px; border-radius: 50%;
    background: var(--white); margin-right: 18px;
    display: flex; align-items: center; justify-content: center;
    box-shadow: 0 3px 4px rgba(0,0,0,0.25);
  }
  .service__badge-inner {
    width: 54px; height: 54px; border-radius: 50%;
    border: 3px solid var(--blue);
    display: flex; align-items: center; justify-content: center;
  }
  .service--wide { align-items: flex-start; }
  .service--wide .service__badge { margin-top: -4px; }

  .contact { position: absolute; left: 46px; top: 474px; list-style: none; }
  .contact__item {
    display: flex; align-items: center; gap: 12px;
    font-family: "Montserrat", sans-serif; font-weight: 700; font-size: 20.5px;
  }
  .contact__item + .contact__item { margin-top: 14px; }
</style>
</head>
<body>
  <div class="sign">
    <section class="sign__main">
      <div class="brand">
        <span class="brand__dot"></span>
        <span class="brand__name">Tidewell</span>
      </div>
      <div class="trades">
        <span class="trades__electrical">Electrical</span>
        <span class="trades__air">Air Conditioning</span>
        <span class="trades__plumbing">Plumbing</span>
      </div>
      <div class="call-rule">
        <span class="call-rule__line"></span>
        <span class="call-rule__icon">
          <svg width="20" height="20" viewBox="0 0 24 24" aria-hidden="true">
            <path d="M6.6 10.8a15.1 15.1 0 0 0 6.6 6.6l2.2-2.2a1 1 0 0 1 1-.25 11.4 11.4 0 0 0 3.6.6 1 1 0 0 1 1 1V20a1 1 0 0 1-1 1A17 17 0 0 1 3 4a1 1 0 0 1 1-1h3.5a1 1 0 0 1 1 1c0 1.25.2 2.45.6 3.6a1 1 0 0 1-.25 1z" fill="none" stroke="#fff" stroke-width="1.8"/>
          </svg>
        </span>
        <span class="call-rule__line"></span>
      </div>
      <div class="phone">0400 517 238</div>
    </section>

    <div class="sign__divider">
      <span class="sign__divider-top"></span>
      <span class="sign__divider-bottom"></span>
    </div>

    <section class="sign__services">
      <ul class="service-list">
        <li class="service">
          <span class="service__badge"><span class="service__badge-inner">
            <svg width="28" height="28" viewBox="0 0 24 24" aria-hidden="true">
              <circle cx="12" cy="12" r="7" fill="none" stroke="#186bb0" stroke-width="3" stroke-dasharray="3 2.5"/>
              <circle cx="12" cy="12" r="3" fill="#186bb0"/>
              <path d="M13 13l7 7" stroke="#e5252a" stroke-width="2.5" stroke-linecap="round"/>
            </svg>
          </span></span>
          Installation
        </li>
        <li class="service">
          <span class="service__badge"><span class="service__badge-inner">
            <svg width="28" height="28" viewBox="0 0 24 24" aria-hidden="true">
              <path d="M12 2l1.2 2.5 2.7.3-2 1.8.6 2.7L12 8l-2.5 1.3.6-2.7-2-1.8 2.7-.3z" fill="#e5252a"/>
              <path d="M5 13h3v9H5zM9 13l3-4c1 0 1.5.7 1.2 1.8L12.8 13H18a1.5 1.5 0 0 1 1.4 2l-1.6 5.5A2 2 0 0 1 16 22H9z" fill="#186bb0"/>
            </svg>
          </span></span>
          Service
        </li>
        <li class="service service--wide">
          <span class="service__badge"><span class="service__badge-inner">
            <svg width="28" height="28" viewBox="0 0 24 24" aria-hidden="true">
              <path d="M4 6a3.5 3.5 0 0 0 4.6 3.3l8.5 8.5a1.6 1.6 0 0 0 2.2-2.2L10.8 7A3.5 3.5 0 0 0 7 3.5L9 5.5 8.5 7.5 6.5 8 4.5 6z" fill="#e5252a"/>
              <path d="M5 15h5l3 3-3 3H5z" fill="#186bb0"/>
            </svg>
          </span></span>
          <span>Repairs and<br>Maintenance</span>
        </li>
      </ul>

      <ul class="contact">
        <li class="contact__item">
          <svg width="20" height="16" viewBox="0 0 20 16" aria-hidden="true">
            <rect x="1.5" y="1.5" width="17" height="13" fill="none" stroke="#fff" stroke-width="2"/>
            <path d="M4 5l6 4 6-4" fill="none" stroke="#fff" stroke-width="2"/>
          </svg>
          info@tidewellelectrical.com.au
        </li>
        <li class="contact__item">
          <svg width="20" height="20" viewBox="0 0 20 20" aria-hidden="true">
            <circle cx="10" cy="10" r="8.5" fill="none" stroke="#fff" stroke-width="2"/>
            <ellipse cx="10" cy="10" rx="3.5" ry="8.5" fill="none" stroke="#fff" stroke-width="1.6"/>
            <path d="M1.5 10h17" stroke="#fff" stroke-width="1.6"/>
          </svg>
          www.tidewellelectrical.com.au
        </li>
      </ul>
    </section>
  </div>
</body>
</html>
```